Custom Mexican Train Dominos Scorecard

My wife and I regularly play Mexican Train dominos with our friends and family and would like to create a series of custom scorecards specific to our various groups that we play with. The idea would be to have them printed on pads or in notebooks that over time will hold a record of all of our games. Searching around on the web, the only "off the shelf" that I see are pretty plain and boring (see attached). We would love something with a fun and playful mid-century graphic feel to it. Can be a single color or more than one. We want to have the player names incorporated into the design, so for the first one the names would be Carla, Douglas, Ruth & Oliver. We will want a place to date each card and of course boxes to fill out the score. I have included a few examples of how the scorecard is basically laid out. Can be any size and can be done in landscape or portrait. I think I would just like the title to say "Domino Night" or potentially no title at all with just a fun domino graphic. Thank you!

Requirements
Must have
• Basic score layout
Nice to have
• nothing in particular
Should not have
• nothing in particular

```html
<!DOCTYPE html>
<html lang="en">
<head>
<meta charset="utf-8">
<title>Domino Night Scorecard</title>
<link rel="stylesheet" href="https://fonts.googleapis.com/css2?family=Arimo:wght@400&display=swap">
<style>
  :root {
    --blue: #4394b6;
    --teal: #62bab6;
    --peach: #f9c9b6;
    --pink: #f7b0b3;
    --mint: #9ed3ae;
    --paper: #ffffff;
    --cream: #fdf8ec;
  }
  * { box-sizing: border-box; margin: 0; padding: 0; }
  html, body { width: 982px; height: 1200px; overflow: hidden; background: var(--paper); }
  body { position: relative; font-family: "Arimo", Arial, sans-serif; }

  .masthead {
    position: absolute; left: 69px; top: 64px; width: 853px; height: 188px;
    background: var(--blue);
    overflow: hidden;
  }
  .masthead-pattern {
    position: absolute; inset: 0;
    background: linear-gradient(90deg, rgba(98,186,182,.55), rgba(249,201,182,.5) 30%, rgba(247,176,179,.5) 55%, rgba(158,211,174,.55) 80%, rgba(98,186,182,.5));
  }
  .title {
    position: absolute; top: 6px; left: 0; right: 0;
    text-align: center; color: var(--paper);
    font-size: 48px; font-weight: 400; letter-spacing: 0.5px;
  }
  .train-mark {
    position: absolute; left: 446px; top: 60px; width: 98px; height: 118px;
    background: var(--cream); border-radius: 10px 10px 6px 6px;
  }

  .scorecard {
    position: absolute; left: 69px; top: 277px; width: 853px; height: 798px;
    display: grid;
    grid-template-columns: repeat(6, 1fr);
    grid-template-rows: 72px repeat(15, 1fr);
    gap: 2px; background: var(--paper);
  }
  .cell { background: var(--blue); display: flex; align-items: center; justify-content: center; color: var(--paper); font-size: 23px; }
  .head { font-size: 22px; line-height: 1.3; text-align: center; }
  .player-1 { color: var(--teal); }
  .player-2 { color: var(--peach); }
  .player-3 { color: var(--pink); }
  .player-4 { color: var(--mint); }
  .score-1 { background: var(--teal); }
  .score-2 { background: var(--peach); }
  .score-3 { background: var(--pink); }
  .score-4 { background: var(--mint); }
  .round { gap: 6px; }
  .round svg { width: 68px; height: 28px; }
  .total { font-size: 23px; }

  .footer-band {
    position: absolute; left: 69px; top: 1094px; width: 853px; height: 56px;
    background: var(--blue);
  }
</style>
</head>
<body>
  <header class="masthead">
    <div class="masthead-pattern" role="img" aria-label="Playful pattern of rounded diamonds in teal, peach, pink and mint"></div>
    <h1 class="title">DOMINO NIGHT</h1>
    <div class="train-mark" role="img" aria-label="Front view of a locomotive"></div>
  </header>

  <svg width="0" height="0" style="position:absolute">
    <defs>
      <symbol id="tile" viewBox="0 0 68 28">
        <rect x="1.5" y="1.5" width="65" height="25" rx="4" fill="none" stroke="#fff" stroke-width="2"/>
        <line x1="34" y1="4" x2="34" y2="24" stroke="#fff" stroke-width="2"/>
      </symbol>
    </defs>
  </svg>

  <main class="scorecard">
    <div class="cell head">Date</div>
    <div class="cell head">Player’s<br>Name</div>
    <div class="cell head player-1">Carla</div>
    <div class="cell head player-2">Douglas</div>
    <div class="cell head player-3">Ruth</div>
    <div class="cell head player-4">Oliver</div>

    <div class="cell"></div><div class="cell round"><svg><use href="#tile"/></svg>12</div><div class="cell score-1"></div><div class="cell score-2"></div><div class="cell score-3"></div><div class="cell score-4"></div>
    <div class="cell"></div><div class="cell round"><svg><use href="#tile"/></svg>11</div><div class="cell score-1"></div><div class="cell score-2"></div><div class="cell score-3"></div><div class="cell score-4"></div>
    <div class="cell"></div><div class="cell round"><svg><use href="#tile"/></svg>10</div><div class="cell score-1"></div><div class="cell score-2"></div><div class="cell score-3"></div><div class="cell score-4"></div>
    <div class="cell"></div><div class="cell round"><svg><use href="#tile"/></svg>9</div><div class="cell score-1"></div><div class="cell score-2"></div><div class="cell score-3"></div><div class="cell score-4"></div>
    <div class="cell"></div><div class="cell round"><svg><use href="#tile"/></svg>8</div><div class="cell score-1"></div><div class="cell score-2"></div><div class="cell score-3"></div><div class="cell score-4"></div>
    <div class="cell"></div><div class="cell round"><svg><use href="#tile"/></svg>7</div><div class="cell score-1"></div><div class="cell score-2"></div><div class="cell score-3"></div><div class="cell score-4"></div>
    <div class="cell"></div><div class="cell round"><svg><use href="#tile"/></svg>5</div><div class="cell score-1"></div><div class="cell score-2"></div><div class="cell score-3"></div><div class="cell score-4"></div>
    <div class="cell"></div><div class="cell total">Sub Total</div><div class="cell score-1"></div><div class="cell score-2"></div><div class="cell score-3"></div><div class="cell score-4"></div>
    <div class="cell"></div><div class="cell round"><svg><use href="#tile"/></svg>6</div><div class="cell score-1"></div><div class="cell score-2"></div><div class="cell score-3"></div><div class="cell score-4"></div>
    <div class="cell"></div><div class="cell round"><svg><use href="#tile"/></svg>4</div><div class="cell score-1"></div><div class="cell score-2"></div><div class="cell score-3"></div><div class="cell score-4"></div>
    <div class="cell"></div><div class="cell round"><svg><use href="#tile"/></svg>3</div><div class="cell score-1"></div><div class="cell score-2"></div><div class="cell score-3"></div><div class="cell score-4"></div>
    <div class="cell"></div><div class="cell round"><svg><use href="#tile"/></svg>2</div><div class="cell score-1"></div><div class="cell score-2"></div><div class="cell score-3"></div><div class="cell score-4"></div>
    <div class="cell"></div><div class="cell round"><svg><use href="#tile"/></svg>1</div><div class="cell score-1"></div><div class="cell score-2"></div><div class="cell score-3"></div><div class="cell score-4"></div>
    <div class="cell"></div><div class="cell round"><svg><use href="#tile"/></svg>0</div><div class="cell score-1"></div><div class="cell score-2"></div><div class="cell score-3"></div><div class="cell score-4"></div>
    <div class="cell"></div><div class="cell total">Game Total</div><div class="cell score-1"></div><div class="cell score-2"></div><div class="cell score-3"></div><div class="cell score-4"></div>
  </main>

  <footer class="footer-band"></footer>
</body>
</html>
```